Welding Fabrication and Inspection Business Card Design

Welding Fabrication and Inspection Services,

Business

Industrial Machinery ServicesMohammed Rahim30 Ballarat Street, Mount Gravatt East.4122.QLD

```html
<!DOCTYPE html>
<html lang="en">
<head>
<meta charset="utf-8">
<title>Corvane Plant Services – Business Card</title>
<link href="https://fonts.googleapis.com/css2?family=Barlow:wght@500;600;700&family=Barlow+Condensed:wght@500&family=Roboto:wght@400&display=swap" rel="stylesheet">
<style>
  :root {
    --stage: #a9a7a8;
    --card: #fbfbfb;
    --ink: #1f1d1d;
    --band: #2a2626;
    --band-text: #ffffff;
    --strip: #707070;
    --divider: #e2e2e2;
  }
  * { margin: 0; padding: 0; box-sizing: border-box; }
  html, body { width: 1200px; height: 1200px; overflow: hidden; }
  body { background: var(--stage); position: relative; font-family: "Barlow", sans-serif; color: var(--ink); }

  .card { position: absolute; background: var(--card); overflow: hidden; }
  .card--front { left: 238px; top: 119px; width: 713px; height: 418px; }
  .card--back { left: 230px; top: 644px; width: 714px; height: 417px; }

  .brand { position: absolute; display: flex; align-items: center; gap: 12px; font-weight: 700; white-space: nowrap; color: var(--ink); }
  .brand__dot { width: 14px; height: 14px; border-radius: 50%; background: var(--ink); }
  .card--front .brand { left: 0; right: 0; top: 160px; justify-content: center; font-size: 34px; }
  .card--back .brand { left: 40px; width: 290px; top: 160px; justify-content: center; font-size: 25px; }
  .card--back .brand__dot { width: 11px; height: 11px; }

  .tagline-band { position: absolute; left: 0; right: 0; bottom: 0; height: 70px; background: var(--band); color: var(--band-text); display: flex; align-items: center; justify-content: center; font-weight: 600; font-size: 24px; letter-spacing: 0.7px; }

  .divider { position: absolute; left: 357px; top: 45px; width: 1px; height: 275px; background: var(--divider); }

  .contact { position: absolute; left: 401px; top: 90px; }
  .contact__name { font-weight: 700; font-size: 28px; letter-spacing: 0.4px; line-height: 1; }
  .contact__role { font-weight: 600; font-size: 16px; margin-top: 8px; letter-spacing: 0.5px; }
  .contact__list { list-style: none; margin-top: 22px; font-family: "Roboto", sans-serif; font-size: 18px; line-height: 25px; }
  .contact__list li { display: flex; align-items: center; gap: 16px; }
  .contact__list svg { width: 18px; height: 14px; fill: var(--ink); flex: none; }
  .contact__address { font-family: "Roboto", sans-serif; font-size: 18px; line-height: 25px; margin-top: 4px; }

  .foot-strip { position: absolute; left: 0; right: 0; bottom: 0; height: 24px; background: var(--strip); }
  .foot-band { position: absolute; right: 0; bottom: 0; width: 440px; height: 53px; }
  .foot-band__text { position: absolute; right: 26px; bottom: 14px; color: var(--band-text); font-family: "Barlow Condensed", sans-serif; font-weight: 500; font-size: 22px; white-space: nowrap; }
</style>
</head>
<body>
  <section class="card card--front">
    <div class="brand"><span class="brand__dot"></span>Corvane Plant Services</div>
    <div class="tagline-band">Welding Fabrication and Inspection Services</div>
  </section>

  <section class="card card--back">
    <div class="brand"><span class="brand__dot"></span>Corvane Plant Services</div>
    <div class="divider"></div>
    <div class="contact">
      <div class="contact__name">Tariq Osmani</div>
      <div class="contact__role">Owner</div>
      <ul class="contact__list">
        <li><svg viewBox="0 0 18 14"><path d="M1 4c0-2 3-3 8-3s8 1 8 3v1h-4V3.5H5V5H1z M4 6h10l2 7H2z"/></svg>+00 555 014 2290</li>
        <li><svg viewBox="0 0 18 14"><path d="M1 1h16v12H1z M2 2l7 6 7-6v1l-7 6-7-6z" fill-rule="evenodd"/></svg>tariq@corvaneplant.example</li>
      </ul>
      <div class="contact__address">17 Windorah Street, Kessling Ridge<br>North. 4670. HVT</div>
    </div>
    <div class="foot-strip"></div>
    <svg class="foot-band" viewBox="0 0 440 53" preserveAspectRatio="none"><polygon points="32,0 440,0 440,53 0,53" fill="var(--band)"/></svg>
    <div class="foot-band__text">Welding Fabrication &amp; Inspection Services</div>
  </section>
</body>
</html>
```